Gather the Marrow Book Cover

Looking for a cover for my book, Gather the Marrow. Part memoir, part self help - this book is one One woman's road away from the good-girl script and home to her wild, sacred inner calling. Think "boss ass bitch" in NYC transitions to Spiritual Goddess to the beaches of Costa Rica. We are playing on the archetypes of Wounded Masculine to Divine Feminine. Breaking the mold of being a good girl and owning her wild.

Target Market(s)

25-35 yr old female

Industry/Entity Type

Personal Development, Memoir

Other font styles liked:
• Pink #ff0099 Yellow #ffdf2b Teal #1fc4cd Gather - Brittany The - open sans Marrow - Bebas Neue

Colors
FFF300
FFF600
FEFA6F
FFFEC7
FFFEE8
E54698
E96AAD
F1A4CE
F9D9EA
FCEFF6

Requirements
Nice to have

```html
<!DOCTYPE html>
<html lang="en">
<head>
<meta charset="utf-8">
<title>Gather the Marrow — Book Cover</title>
<link href="https://fonts.googleapis.com/css2?family=Bebas+Neue&family=Open+Sans:ital,wght@1,400&family=Sacramento&display=swap" rel="stylesheet">
<style>
  :root {
    --stage: #000000;
    --magenta: #ea168e;
    --sun-light: #f8e533;
    --sun-mid: #f7b52c;
    --sun-deep: #f2792c;
    --subtitle: #f6ee7a;
    --ink: #050505;
  }
  html, body {
    margin: 0;
    width: 928px;
    height: 1200px;
    overflow: hidden;
    background: var(--stage);
  }
  .cover {
    position: absolute;
    left: 137px;
    top: 108px;
    width: 655px;
    height: 982px;
    overflow: hidden;
    background: linear-gradient(150deg, var(--sun-light) 0%, var(--sun-mid) 50%, var(--sun-deep) 100%);
  }
  .cover-art {
    position: absolute;
    inset: 0;
    width: 655px;
    height: 982px;
  }
  .subtitle {
    position: absolute;
    right: 54px;
    top: 62px;
    margin: 0;
    font-family: "Bebas Neue", sans-serif;
    font-weight: 400;
    font-size: 39px;
    line-height: 40px;
    text-align: right;
    color: var(--subtitle);
    letter-spacing: 0.2px;
  }
  .title {
    margin: 0;
    font-weight: 400;
    color: var(--ink);
  }
  .title-script {
    position: absolute;
    left: 122px;
    top: 415px;
    font-family: "Sacramento", cursive;
    font-size: 160px;
    line-height: 1;
  }
  .title-joiner {
    position: absolute;
    left: 400px;
    top: 608px;
    font-family: "Open Sans", sans-serif;
    font-style: italic;
    font-size: 42px;
    line-height: 1;
  }
  .title-block {
    position: absolute;
    left: 0;
    width: 655px;
    top: 712px;
    text-align: center;
    font-family: "Bebas Neue", sans-serif;
    font-size: 188px;
    line-height: 1;
    letter-spacing: 2px;
  }
</style>
</head>
<body>
  <main class="cover">
    <svg class="cover-art" viewBox="0 0 655 982" xmlns="http://www.w3.org/2000/svg">
      <path class="sky-band" d="M0,0 H655 V288 C540,290 420,370 296,396 C220,410 120,400 0,374 Z" fill="var(--magenta)"/>
      <path class="wave-line" d="M0,374 C120,400 220,410 296,396 C420,370 540,290 655,272 V288 C540,290 420,370 296,396 C220,410 120,400 0,379 Z" fill="var(--ink)"/>
      <rect class="portrait-area" role="img" aria-label="Yellow silhouette of a woman with her hair in a bun, rising out of the wave" x="102" y="142" width="151" height="250" rx="60" fill="var(--sun-light)"/>
    </svg>
    <p class="subtitle">One woman's road away from<br>the good-girl script and<br>home to her wild, sacred<br>inner calling</p>
    <h1 class="title">
      <span class="title-script">Gather</span>
      <span class="title-joiner">the</span>
      <span class="title-block">MARROW</span>
    </h1>
  </main>
</body>
</html>
```